The BRV Relational Philanthropy Cycle

The title for this graphic is above. It must be included.
I am looking for a graphic representation of the relationship between the Christian school and the donor / pointing to the child (student) - the school's mission / outcome of investment through a gift / appreciation of the gift / communication of the gift impact for the child / stronger relationship going back to the child. This is not easy to do. I've tried to do it on my own and can't get it.
Any cliched child representations will be dismissed out of hand e.g. mortar boards, pencils, uniforms etc. The child should be abstract so that gender and race are irrelevant.
The key to this whole thing is the idea of RELATIONSHIP. The close relationship of donor and the Christian school, the pointing of that relationship to focus on the child / the school's mission, the outpouring of generosity that then happens in the heart of the donor and the gift that results, followed up by intentional work by the Christian school to thank and inform the donor - thank for the gift inform about the gift's expenditure and impact in the life of the child - all of which leads to a strengthening of the relationship and continued philanthropy as a never ending cycle.
It must be branded - logo and colors attached.
It must be obvious - easy to grasp the basic idea of relationship resulting in generosity / philanthropy. The visual should be clear - any words used illustrate - I should not 'need' the words to understand the idea.
I need it on a PP slide, jpeg, thumbnail. It must be highly legible in no more than 1/3 of a regular size piece of paper.
Our website is harborlightacademyguild.example
google donor cultivation cycle or donor giving cycle to see many examples of cycles that are used in secular contexts - the big difference in BRV's is the focus on the child and the importance of the relationship.

```html
<!DOCTYPE html>
<html lang="en">
<head>
<meta charset="utf-8">
<title>The BRV Relational Philanthropy Cycle</title>
<link rel="stylesheet" href="https://fonts.googleapis.com/css2?family=EB+Garamond:wght@600&family=Montserrat:wght@500;600;700;800&display=swap">
<style>
  :root {
    --brand-blue: #4376aa;
    --ring-blue: #87a8ca;
    --donor-orange: #eca046;
    --steward-green: #6aad48;
    --label-grey: #6e6e6e;
    --white: #ffffff;
    --paper: #ffffff;
  }
  html, body {
    margin: 0;
    padding: 0;
    width: 1200px;
    height: 1199px;
    overflow: hidden;
    background: var(--paper);
  }
  .cycle-graphic {
    display: block;
    width: 1200px;
    height: 1199px;
  }
  .title {
    font-family: "EB Garamond", Georgia, serif;
    font-weight: 600;
    font-size: 84px;
    fill: var(--brand-blue);
  }
  .arc-label {
    font-family: "Montserrat", Arial, sans-serif;
    font-weight: 500;
    font-size: 48px;
    letter-spacing: 1px;
    fill: var(--label-grey);
  }
  .verse-label {
    font-family: "Montserrat", Arial, sans-serif;
    font-weight: 500;
    font-size: 47px;
    fill: var(--white);
  }
  .node-label {
    font-family: "Montserrat", Arial, sans-serif;
    font-weight: 800;
    font-size: 48px;
    fill: var(--white);
    text-anchor: middle;
  }
  .flow-arc { fill: none; stroke: var(--brand-blue); stroke-width: 66; }
  .flow-head, .flow-chevron { fill: var(--brand-blue); }
  .icon { fill: none; stroke: var(--white); stroke-width: 4.5; stroke-linecap: round; stroke-linejoin: round; }
  .copyright {
    font-family: "Montserrat", Arial, sans-serif;
    font-weight: 500;
    font-size: 40px;
    fill: var(--label-grey);
  }
  .brand-name {
    font-family: "Montserrat", Arial, sans-serif;
    font-weight: 600;
    font-size: 40px;
    fill: var(--label-grey);
    text-anchor: end;
  }
</style>
</head>
<body>
<svg class="cycle-graphic" viewBox="0 0 1920 1918" xmlns="http://www.w3.org/2000/svg" aria-labelledby="graphic-title">
  <title id="graphic-title">The BRV Relational Philanthropy Cycle</title>
  <defs>
    <path id="path-inspired" d="M413 1022 A552 552 0 0 1 1517 1022"/>
    <path id="path-mission" d="M365 1022 A600 600 0 0 0 1565 1022"/>
    <path id="path-luke" d="M690 1022 A275 275 0 0 1 1240 1022"/>
    <path id="path-mark" d="M655 1022 A310 310 0 0 0 1275 1022"/>
    <g id="double-chevron">
      <polygon points="-16,-15 7,0 -16,15"/>
      <polygon points="3,-15 26,0 3,15"/>
    </g>
  </defs>

  <text class="title" x="965" y="262" text-anchor="middle">The BRV Relational Philanthropy Cycle</text>

  <path class="flow-arc" d="M528 780 A500 500 0 0 1 1359 714"/>
  <polygon class="flow-head" points="1418,692 1413,792 1320,755"/>
  <path class="flow-arc" d="M1402 1264 A500 500 0 0 1 571 1330"/>
  <polygon class="flow-head" points="512,1352 517,1252 610,1289"/>

  <text class="arc-label"><textPath href="#path-inspired" startOffset="50%" text-anchor="middle">Inspired Giving</textPath></text>
  <text class="arc-label"><textPath href="#path-mission" startOffset="50%" text-anchor="middle">Mission Based Relationship</textPath></text>

  <circle cx="965" cy="1022" r="375" fill="var(--ring-blue)"/>
  <text class="verse-label"><textPath href="#path-luke" startOffset="50%" text-anchor="middle">Luke 8:3</textPath></text>
  <text class="verse-label"><textPath href="#path-mark" startOffset="50%" text-anchor="middle">Mark 9:37</textPath></text>

  <g class="flow-chevron">
    <use href="#double-chevron" transform="translate(740 822) rotate(-45)"/>
    <use href="#double-chevron" transform="translate(1202 826) rotate(45)"/>
    <use href="#double-chevron" transform="translate(1200 1228) rotate(135)"/>
    <use href="#double-chevron" transform="translate(736 1230) rotate(225)"/>
  </g>

  <g class="node node-donor">
    <circle cx="522" cy="1022" r="222" fill="var(--donor-orange)"/>
    <g class="icon">
      <path d="M516 970 L488 942 C474 928 484 912 498 912 C508 912 514 920 516 926 C518 920 524 912 534 912 C548 912 558 928 544 942 Z"/>
      <path d="M462 1020 L488 994 C494 988 500 986 508 986 L540 986 C548 986 548 998 540 998 L514 998"/>
      <path d="M462 1020 L480 1038 L488 1032 L550 1028 L580 1000 C584 994 576 986 570 990 L542 1010 L512 1012"/>
    </g>
    <text class="node-label" x="522" y="1110">DONOR</text>
  </g>

  <g class="node node-steward">
    <circle cx="1410" cy="1022" r="222" fill="var(--steward-green)"/>
    <g class="icon">
      <path d="M1366 976 A44 44 0 1 1 1454 976"/>
      <path d="M1366 962 L1454 962 M1362 976 L1458 976"/>
      <path d="M1410 932 L1410 978 M1392 976 C1384 952 1392 936 1410 932 C1428 936 1436 952 1428 976"/>
      <path d="M1468 1020 L1442 994 C1436 988 1430 986 1422 986 L1390 986 C1382 986 1382 998 1390 998 L1416 998"/>
      <path d="M1468 1020 L1450 1038 L1442 1032 L1380 1028 L1350 1000 C1346 994 1354 986 1360 990 L1388 1010 L1418 1012"/>
    </g>
    <text class="node-label" x="1410" y="1098">DONOR</text>
    <text class="node-label" x="1410" y="1158">STEWARD</text>
  </g>

  <g class="node node-child">
    <circle cx="965" cy="1022" r="244" fill="var(--brand-blue)" stroke="rgba(70,80,95,0.45)" stroke-width="10"/>
    <g class="icon">
      <circle cx="965" cy="934" r="15"/>
      <path d="M950 962 C950 952 980 952 980 962 L976 1022 C975 1030 955 1030 954 1022 Z"/>
      <circle cx="924" cy="952" r="12"/>
      <path d="M911 974 C911 964 937 964 937 974 L932 1022 C931 1030 917 1030 916 1022 Z"/>
      <circle cx="1006" cy="952" r="12"/>
      <path d="M993 974 C993 964 1019 964 1019 974 L1014 1022 C1013 1030 999 1030 998 1022 Z"/>
    </g>
    <text class="node-label" x="965" y="1110">THE CHILD</text>
  </g>

  <text class="copyright" x="205" y="1837">© Harbor Light Academy Guild 2022</text>

  <text class="brand-name" x="1716" y="1837">BRV</text>
</svg>
</body>
</html>
```